Women's Online Clothing Boutique Needs Business Cards

I already have a logo that I would like to use. Some of the things that interest me is black business cards, foil embossed logo, glossy embossed logo, leopard print, no yellow font, rounded edges. I even like just a large logo on the front side with all of my information on the back side.

Contact Information for Business Card

https://silverheron.shopvenlo.com/
https://www.pagelink.net/thesilverheronboutique/
https://www.picfeed.net/thesilverheronboutique/
silverheronboutique@mailora.net

Requirements
Must have
• My Logo
Nice to have
• Leopard Print
Should not have
• No Yellow Font

```html
<!DOCTYPE html>
<html lang="en">
<head>
<meta charset="utf-8">
<title>The Silver Heron Boutique – Business Cards</title>
<link rel="stylesheet" href="https://fonts.googleapis.com/css2?family=Poppins:wght@400&display=swap">
<style>
  :root {
    --backdrop: #4b5053;
    --card: #050505;
    --ink: #ffffff;
    --ink-soft: #e9e9e9;
    --shadow: rgba(0, 0, 0, 0.45);
  }
  * { box-sizing: border-box; margin: 0; padding: 0; }
  html, body {
    width: 1200px;
    height: 1050px;
    overflow: hidden;
    background: var(--backdrop);
    font-family: "Poppins", sans-serif;
    color: var(--ink);
  }
  .sheet {
    width: 1200px;
    height: 1050px;
    display: flex;
    flex-direction: column;
    align-items: center;
    justify-content: center;
    gap: 34px;
  }
  .card {
    width: 840px;
    height: 480px;
    background: var(--card);
    border-radius: 18px;
    box-shadow: 0 10px 28px var(--shadow);
    position: relative;
    overflow: hidden;
  }
  /* Front */
  .card--front {
    display: flex;
    align-items: center;
    justify-content: center;
  }
  .wordmark {
    display: flex;
    flex-direction: column;
    align-items: center;
    gap: 14px;
  }
  .wordmark__badge {
    width: 26px;
    height: 26px;
    border-radius: 50%;
    background: var(--ink);
  }
  .wordmark__name {
    font-size: 50px;
    font-weight: 400;
    letter-spacing: -0.5px;
    line-height: 1;
    white-space: nowrap;
  }
  .wordmark__rule {
    width: 440px;
    height: 1px;
    background: var(--ink);
    opacity: 0.8;
  }
  /* Back */
  .card--back {
    padding: 78px 0 0 150px;
  }
  .back__title {
    font-size: 36px;
    font-weight: 400;
    letter-spacing: -0.3px;
    line-height: 1;
    margin-bottom: 46px;
    white-space: nowrap;
  }
  .contacts {
    list-style: none;
    display: flex;
    flex-direction: column;
    gap: 22px;
  }
  .contact {
    display: flex;
    align-items: center;
    gap: 34px;
    font-size: 22px;
    color: var(--ink-soft);
  }
  .contact__icon {
    width: 36px;
    height: 36px;
    flex: none;
    display: flex;
    align-items: center;
    justify-content: center;
  }
  .contact__icon svg { width: 36px; height: 36px; }
  .contact__mark {
    width: 28px;
    height: 28px;
    border: 2.5px solid var(--ink);
    border-radius: 6px;
  }
  .card__dot {
    position: absolute;
    left: 22px;
    top: 262px;
    width: 10px;
    height: 10px;
    background: var(--ink);
  }
</style>
</head>
<body>
<main class="sheet">
  <section class="card card--front" aria-label="Card front">
    <div class="wordmark">
      <span class="wordmark__badge" aria-hidden="true"></span>
      <span class="wordmark__name">The Silver Heron Boutique</span>
      <span class="wordmark__rule" aria-hidden="true"></span>
    </div>
  </section>

  <section class="card card--back" aria-label="Card back">
    <span class="card__dot" aria-hidden="true"></span>
    <h1 class="back__title">The Silver Heron Boutique</h1>
    <ul class="contacts">
      <li class="contact">
        <span class="contact__icon">
          <svg viewBox="0 0 36 36" aria-hidden="true">
            <rect x="3" y="7" width="30" height="22" fill="none" stroke="#fff" stroke-width="2.5"/>
            <path d="M3 7 L18 20 L33 7 M3 29 L14 17 M33 29 L22 17" fill="none" stroke="#fff" stroke-width="2"/>
          </svg>
        </span>
        <span>silverheronboutique@mailora.net</span>
      </li>
      <li class="contact">
        <span class="contact__icon">
          <svg viewBox="0 0 36 36" aria-hidden="true">
            <circle cx="18" cy="18" r="14" fill="none" stroke="#fff" stroke-width="2.5"/>
            <ellipse cx="18" cy="18" rx="6" ry="14" fill="none" stroke="#fff" stroke-width="2"/>
            <path d="M4 18 H32 M6 11 H30 M6 25 H30 M18 4 V32" fill="none" stroke="#fff" stroke-width="2"/>
          </svg>
        </span>
        <span>www.silverheron.shopvenlo.com</span>
      </li>
      <li class="contact">
        <span class="contact__icon"><span class="contact__mark" aria-hidden="true"></span></span>
        <span>@thesilverheronboutique</span>
      </li>
      <li class="contact">
        <span class="contact__icon"><span class="contact__mark" aria-hidden="true"></span></span>
        <span>@thesilverheronboutique</span>
      </li>
    </ul>
  </section>
</main>
</body>
</html>
```